Animal Eye Clinic needs a Business card

We are a new veterinary ophthalmology practice (Tessaly Animal Eye Care) and we need a business card designed. We only see animal eyes - we are not a regular veterinary clinic. We already have a logo. We are looking for a professional, good looking business card to hand out to our clients. We are looking for something simple but professional and contemporary. Our logo is likely the only picture/graphic that needs to be on the card.
Updates

Contact Information for Business Card

Marisol Dunkley, BSc, DVM, MSc, DipACVO
Veterinary Ophthalmologist

Phone: 250.418.3097
Email: tessalyanimaleyecare@mailbrook.net
Website: tessalyanimaleyecare.net
Address: 1840 Pellworth Rd
Kelowna, BC, V4T 8M3

Colors

Designer to choose colors to be used in the design.

Requirements
Must have
• Our logo (attached)

```html
<!DOCTYPE html>
<html lang="en">
<head>
<meta charset="utf-8">
<title>Tessaly Animal Eye Care — Business Card</title>
<link rel="stylesheet" href="https://fonts.googleapis.com/css2?family=Lato:wght@300;400;700&display=swap">
<style>
  :root {
    --page: #e9ebec;
    --card-dark: #2a2a2b;
    --pattern-tone: #3a3a3c;
    --teal: #1597a6;
    --teal-deep: #0f8593;
    --swoosh: #8c8c8e;
    --white: #ffffff;
    --ink-light: #dff3f5;
    --muted: #9a9a9c;
  }
  * { box-sizing: border-box; margin: 0; padding: 0; }
  html, body {
    width: 1200px; height: 900px; overflow: hidden;
    background: var(--page);
    font-family: "Lato", sans-serif;
  }
  .stage {
    position: relative; width: 1200px; height: 900px;
  }
  .card {
    position: absolute; left: 250px; width: 700px; height: 400px;
    border-radius: 18px; overflow: hidden;
    box-shadow: 0 6px 18px rgba(0,0,0,.18);
  }
  /* Back side */
  .card-back { top: 35px; background: var(--card-dark); }
  .paw-pattern {
    position: absolute; inset: 0;
    background: radial-gradient(circle at 50% 50%, var(--pattern-tone), var(--card-dark) 80%);
  }
  .back-brand {
    position: absolute; left: 0; right: 0; top: 150px;
    display: flex; align-items: center; justify-content: center; gap: 16px;
  }
  .brand-dot {
    width: 26px; height: 26px; border-radius: 50%; background: var(--white);
  }
  .back-brand .brand-name {
    color: var(--white); font-weight: 700; font-size: 34px; letter-spacing: .5px;
  }
  .back-web {
    position: absolute; left: 0; right: 0; top: 300px; text-align: center;
    color: var(--white); font-size: 15px; letter-spacing: 3px; font-weight: 400;
  }
  /* Front side */
  .card-front { top: 465px; background: var(--white); }
  .front-shapes { position: absolute; inset: 0; }
  .front-brand {
    position: absolute; left: 70px; top: 70px;
    display: flex; align-items: center; gap: 14px;
  }
  .front-brand .brand-dot { background: var(--teal); width: 30px; height: 30px; }
  .front-brand .brand-name {
    color: var(--teal); font-weight: 700; font-size: 30px; letter-spacing: .3px;
  }
  .person {
    position: absolute; right: 46px; top: 170px; text-align: right; color: var(--white);
  }
  .person-name { font-weight: 700; font-size: 19px; letter-spacing: .5px; text-transform: uppercase; }
  .person-creds { font-weight: 300; font-size: 14px; margin-top: 4px; color: var(--ink-light); }
  .person-title { font-weight: 700; font-size: 14px; margin-top: 5px; }
  .contacts {
    position: absolute; left: 48px; bottom: 34px; color: var(--white);
    font-size: 14px; line-height: 1.7;
  }
  .contact-line { display: flex; align-items: center; gap: 10px; }
  .contact-line svg { width: 14px; height: 14px; fill: var(--white); flex: none; }
  .contact-address { font-weight: 700; font-size: 15px; padding-left: 24px; }
</style>
</head>
<body>
<main class="stage">
  <section class="card card-back">
    <div class="paw-pattern" role="img" aria-label="Repeating grey paw print pattern on charcoal"></div>
    <div class="back-brand">
      <span class="brand-dot"></span>
      <span class="brand-name">Tessaly Animal Eye Care</span>
    </div>
    <p class="back-web">www.tessalyanimaleyecare.net</p>
  </section>

  <section class="card card-front">
    <svg class="front-shapes" viewBox="0 0 700 400" preserveAspectRatio="none" aria-hidden="true">
      <path d="M0,300 C200,240 440,150 700,110 L700,400 L0,400 Z" fill="var(--teal)"/>
      <path d="M150,272 C260,190 400,140 540,128 C410,150 280,200 158,276 Z" fill="var(--swoosh)"/>
    </svg>

    <div class="front-brand">
      <span class="brand-dot"></span>
      <span class="brand-name">Tessaly Animal Eye Care</span>
    </div>

    <div class="person">
      <p class="person-name">Marisol Dunkley</p>
      <p class="person-creds">BSc, DVM, MSc, DipACVO</p>
      <p class="person-title">Veterinary Ophthalmologist</p>
    </div>

    <div class="contacts">
      <p class="contact-line">
        <svg viewBox="0 0 24 24"><path d="M6.6 10.8a15 15 0 0 0 6.6 6.6l2.2-2.2a1 1 0 0 1 1-.25 11.4 11.4 0 0 0 3.6.57 1 1 0 0 1 1 1V20a1 1 0 0 1-1 1A17 17 0 0 1 3 4a1 1 0 0 1 1-1h3.5a1 1 0 0 1 1 1c0 1.25.2 2.45.57 3.57a1 1 0 0 1-.25 1z"/></svg>
        <span>250.418.3097</span>
      </p>
      <p class="contact-line">
        <svg viewBox="0 0 24 24"><path d="M2 5h20v14H2z M4 7v.5l8 5 8-5V7z" fill-rule="evenodd"/></svg>
        <span>tessalyanimaleyecare@mailbrook.net</span>
      </p>
      <p class="contact-address">1840 Pellworth Rd, Kelowna, BC, V4T 8M3</p>
    </div>
  </section>
</main>
</body>
</html>
```